HOT TUB - SPAS service needs an business card

I need an business for my company who his specialise in a maintenance,water treatment and cleaning of Hot Tub - Spas for commercial and residential customers. The company operate mainly in the ski resort of Chamonix, Megève and St Gervais. The final product should communicate pure water, cleanest and professional for luxury property's.
I have upload a logo but any improvement on it is welcome.(color,size, details etc..) or any other idea. Thank you
Company Name: 58 BAINS
My name: Mathieu Rocheval
Email: rochemat@mailnuage.net
Tel: +33 (0)6 58 27 91 06
Description to be on the card in french(first langage) and in English:
- Spas service
- Entretien, traitement eau, nettoyage.
- Maintenance, water treatment, cleaning.

```html
<!DOCTYPE html>
<html lang="fr">
<head>
<meta charset="utf-8">
<title>58 BAINS – Carte de visite</title>
<link rel="stylesheet" href="https://fonts.googleapis.com/css2?family=Oswald:wght@500;600&family=Carlito&display=swap">
<style>
  :root {
    --page: #ffffff;
    --card-border: #2a2a2a;
    --water-light: #c4dfe1;
    --water-mid: #b3d0d3;
    --water-deep: #a6c3c7;
    --brand-blue: #1f4e85;
    --tagline-grey: #4b4b4b;
  }
  html, body {
    margin: 0;
    padding: 0;
    width: 1200px;
    height: 1000px;
    overflow: hidden;
    background: var(--page);
  }
  .canvas {
    position: relative;
    width: 1200px;
    height: 1000px;
  }
  .card {
    position: absolute;
    left: 204px;
    width: 792px;
    box-sizing: border-box;
    border: 1px solid var(--card-border);
    overflow: hidden;
  }
  .card--front { top: 12px; height: 485px; }
  .card--back  { top: 502px; height: 486px; }
  .water-backdrop {
    position: absolute;
    inset: 0;
    background:
      radial-gradient(ellipse 60% 40% at 25% 30%, var(--water-light), transparent 70%),
      radial-gradient(ellipse 50% 45% at 80% 70%, var(--water-deep), transparent 70%),
      linear-gradient(160deg, var(--water-light), var(--water-mid) 55%, var(--water-deep));
  }
  .card-content {
    position: absolute;
    inset: 0;
    text-align: center;
  }
  .brand-name {
    position: absolute;
    left: 0; right: 0;
    top: 210px;
    margin: 0;
    font-family: "Oswald", sans-serif;
    font-weight: 600;
    font-size: 46px;
    letter-spacing: 5px;
    color: var(--brand-blue);
    line-height: 1;
  }
  .tagline {
    position: absolute;
    left: 0; right: 0;
    top: 292px;
    margin: 0;
    font-family: "Carlito", sans-serif;
    font-size: 26px;
    line-height: 30.5px;
    color: var(--tagline-grey);
  }
  .tagline span { display: block; }
  .contact {
    position: absolute;
    left: 0; right: 0;
    top: 190px;
    font-family: "Oswald", sans-serif;
    font-weight: 500;
    color: var(--brand-blue);
    line-height: 1;
  }
  .contact-name {
    margin: 0;
    font-size: 28px;
    letter-spacing: 5.5px;
    text-transform: uppercase;
  }
  .contact-email {
    margin: 8px 0 0;
    font-size: 19px;
    letter-spacing: 3.6px;
    text-transform: uppercase;
  }
  .contact-phone {
    margin: 8px 0 0;
    font-size: 18px;
    letter-spacing: 2px;
  }
</style>
</head>
<body>
<div class="canvas">
  <section class="card card--front">
    <div class="water-backdrop" role="img" aria-label="Photo de surface d'eau turquoise claire en fond de carte"></div>
    <div class="card-content">
      <h1 class="brand-name">58 BAINS</h1>
      <p class="tagline">
        <span>Spas Service</span>
        <span>Entretien | Traitement eau | Nettoyage</span>
        <span>Maintenance | Water treatment | Cleaning</span>
      </p>
    </div>
  </section>

  <section class="card card--back">
    <div class="water-backdrop" role="img" aria-label="Photo de surface d'eau turquoise claire en fond de carte"></div>
    <div class="card-content">
      <div class="contact">
        <p class="contact-name">Mathieu Rocheval</p>
        <p class="contact-email">rochemat@mailnuage.net</p>
        <p class="contact-phone">+33 (0)6 58 27 91 06</p>
      </div>
    </div>
  </section>
</div>
</body>
</html>
```